Premium Packaging Design for a Line of Four Beeswax Candle Scents

Need to design a beeswax quality candle design for ceramic and tube packaging. The ceramic jar size is 11oz (311g) and should be on the label with reference to hand poured or hand crafted.
4 scents that match our branding for our incense. Scents are : 1) AMBER MEADOW 2) GOLDEN ORCHARD 3) VELVET BLOOM 4) MIDNIGHT ROAST. Each tube must have elements of each of its scents i.e MIDNIGHT ROAST should make reference to coffee. Die Line for the candle packaging sizing is attached in files. Design is for the tube packaging only. Must include warning label on the bottom with barcode (dummy barcode can be used for design phase). Logo and other design elements can be taken from .ai incense box. Elements of bees such as wax comb or hexagonal shapes should be used.
Bottom Warning Label (text):
1) Warning Triangle should be in Yellow
2) Icons (attached should be used)
3) Wording:
Always burn within sight and never in drafty conditions
Keep away from things that catch fire
Keep away from children and pets
4) Burn Instructions
Trim wick to 1/4" each time candle is lit. Keep wax pool free of debris including matches and wick trimmings. Only burn candle on level fire resistant surface. Do not burn candle for more than 4 hours at a time.

Target Market(s)

USA market. Must have MADE IN USA on packaging

Industry/Entity Type

Health and Beauty

Font styles to use
Decorative
Script

Requirements
Must have
• Gold stamping
Nice to have
• Follow branded guidelines as per our incense box
Should not have
• cheap and generic stock images

```html
<!DOCTYPE html>
<html lang="en">
<head>
<meta charset="utf-8">
<title>Solvaren Natural Beeswax Candle Tubes</title>
<link href="https://fonts.googleapis.com/css2?family=Cinzel:wght@400;600&display=swap" rel="stylesheet">
<style>
  :root {
    --bg: #161616;
    --tube: #2b2a22;
    --tube-lid: #2e2d25;
    --seam: #1e1d18;
    --gold: #c9a85c;
    --lavender: #6a3fb0;
    --coconut: #d8d8d8;
    --rose: #c8233a;
    --espresso: #5a4440;
  }
  html, body {
    margin: 0;
    padding: 0;
    width: 1200px;
    height: 447px;
    overflow: hidden;
    background: var(--bg);
  }
  .lineup {
    position: relative;
    width: 1200px;
    height: 447px;
  }
  .tube-label {
    position: absolute;
    top: 84px;
    width: 226px;
    height: 266px;
    background: var(--tube);
    font-family: "Cinzel", serif;
    color: var(--gold);
    text-align: center;
    overflow: hidden;
  }
  .tube-label--meadow  { left: 58px;  --accent: var(--lavender); }
  .tube-label--orchard { left: 344px; --accent: var(--coconut); }
  .tube-label--bloom   { left: 628px; --accent: var(--rose); }
  .tube-label--roast   { left: 916px; --accent: var(--espresso); }

  .lid-band {
    position: absolute;
    left: 0; top: 0;
    width: 100%;
    height: 91px;
    background: var(--tube-lid);
    border-bottom: 1px solid var(--seam);
  }
  .brand-name {
    position: absolute;
    left: 0; right: 0;
    top: 48px;
    margin: 0;
    font-size: 20px;
    font-weight: 600;
    letter-spacing: 0.5px;
    line-height: 1;
  }
  .comb-pattern {
    position: absolute;
    left: 0; right: 0;
    bottom: 0;
    height: 130px;
    background: linear-gradient(to bottom, transparent 0%, var(--accent) 160%);
    opacity: 0.35;
  }
  .hex-frame {
    position: absolute;
    left: 0; top: 0;
    width: 226px;
    height: 266px;
  }
  .hex-frame polygon {
    fill: var(--tube);
    stroke: var(--accent);
    stroke-width: 1.6;
  }
  .label-copy {
    position: absolute;
    left: 0; right: 0;
    margin: 0;
    line-height: 1;
  }
  .label-copy--type {
    top: 124px;
    font-size: 7.5px;
    font-weight: 600;
    letter-spacing: 0.2px;
  }
  .label-copy--scent {
    top: 154px;
    font-size: 19px;
    line-height: 21px;
    font-weight: 600;
    letter-spacing: -0.3px;
  }
  .label-copy--craft {
    top: 214px;
    font-size: 7.5px;
    letter-spacing: 0.2px;
  }
  .label-copy--weight {
    top: 232px;
    font-size: 6px;
    font-family: "Times New Roman", serif;
  }
</style>
</head>
<body>
<main class="lineup">

  <section class="tube-label tube-label--meadow">
    <div class="lid-band"></div>
    <h2 class="brand-name">SOLVAREN</h2>
    <div class="comb-pattern" role="img" aria-label="Honeycomb pattern in lavender purple"></div>
    <svg class="hex-frame" viewBox="0 0 226 266" aria-hidden="true"><polygon points="38,175 75,105 151,105 188,175 151,244 75,244"/></svg>
    <p class="label-copy label-copy--type">NATURAL BEESWAX</p>
    <h3 class="label-copy label-copy--scent">AMBER<br>MEADOW</h3>
    <p class="label-copy label-copy--craft">HANDCRAFTED</p>
    <p class="label-copy label-copy--weight">11oz (311g)</p>
  </section>

  <section class="tube-label tube-label--orchard">
    <div class="lid-band"></div>
    <h2 class="brand-name">SOLVAREN</h2>
    <div class="comb-pattern" role="img" aria-label="Honeycomb pattern in silver white"></div>
    <svg class="hex-frame" viewBox="0 0 226 266" aria-hidden="true"><polygon points="38,175 75,105 151,105 188,175 151,244 75,244"/></svg>
    <p class="label-copy label-copy--type">NATURAL BEESWAX</p>
    <h3 class="label-copy label-copy--scent">GOLDEN<br>ORCHARD</h3>
    <p class="label-copy label-copy--craft">HANDCRAFTED</p>
    <p class="label-copy label-copy--weight">11oz (311g)</p>
  </section>

  <section class="tube-label tube-label--bloom">
    <div class="lid-band"></div>
    <h2 class="brand-name">SOLVAREN</h2>
    <div class="comb-pattern" role="img" aria-label="Honeycomb pattern in rose red"></div>
    <svg class="hex-frame" viewBox="0 0 226 266" aria-hidden="true"><polygon points="38,175 75,105 151,105 188,175 151,244 75,244"/></svg>
    <p class="label-copy label-copy--type">NATURAL BEESWAX</p>
    <h3 class="label-copy label-copy--scent">VELVET<br>BLOOM</h3>
    <p class="label-copy label-copy--craft">HANDCRAFTED</p>
    <p class="label-copy label-copy--weight">11oz (311g)</p>
  </section>

  <section class="tube-label tube-label--roast">
    <div class="lid-band"></div>
    <h2 class="brand-name">SOLVAREN</h2>
    <div class="comb-pattern" role="img" aria-label="Honeycomb pattern in espresso brown"></div>
    <svg class="hex-frame" viewBox="0 0 226 266" aria-hidden="true"><polygon points="38,175 75,105 151,105 188,175 151,244 75,244"/></svg>
    <p class="label-copy label-copy--type">NATURAL BEESWAX</p>
    <h3 class="label-copy label-copy--scent">MIDNIGHT<br>ROAST</h3>
    <p class="label-copy label-copy--craft">HANDCRAFTED</p>
    <p class="label-copy label-copy--weight">11oz (311g)</p>
  </section>

</main>
</body>
</html>
```